BrightOak Lending Needs a Stated Income Flyer

We need a flyer created for our Stated Income loan program, using the color scheme to match our company logo.
I've included a stock photo to be used and within that photo, we want Funded stamped in red on the blank poster board.
For the written part of the flyer, we want the word State Income in red.
On the bottom part (Contact Us), we want to make it possible for us to edit for any future loan officer we hire along the way to include their contact information.
We like the flyer for VeroCredit.
Industry/Entity Type
Loan

```html
<!DOCTYPE html>
<html lang="en">
<head>
<meta charset="utf-8">
<title>BrightOak Lending – Stated Income Flyer</title>
<link rel="stylesheet" href="https://fonts.googleapis.com/css2?family=Roboto+Slab:wght@700;800&family=Open+Sans:wght@400;600;700;800&family=Black+Ops+One&display=swap">
<style>
  :root{
    --navy:#0d3f8f;
    --navy-deep:#082e6e;
    --red:#d71f2b;
    --stamp:#d8323a;
    --paper:#ffffff;
    --ink:#1d2f5c;
    --fine:#6b7385;
    --canvas:#e9eaec;
  }
  *{box-sizing:border-box;margin:0;padding:0}
  html,body{width:1200px;height:800px;overflow:hidden}
  body{background:var(--canvas);font-family:"Open Sans",Arial,sans-serif;position:relative}
  .flyer{position:absolute;left:300px;top:20px;width:600px;height:760px;background:var(--paper);overflow:hidden;box-shadow:0 2px 10px rgba(0,0,0,.15)}
  .hero-photo{position:absolute;left:0;top:0;width:600px;height:330px;
    background:linear-gradient(180deg,#f4f2ef 0%,#d9cfc4 45%,#8d8f9c 100%)}
  .poster-board{position:absolute;left:44px;top:150px;width:220px;height:150px;background:#fbfbfb;transform:rotate(-1deg)}
  .stamp{position:absolute;left:44px;top:170px;width:220px;text-align:center;font-family:"Black Ops One",sans-serif;color:var(--stamp);font-size:38px;line-height:1.05;letter-spacing:2px;transform:rotate(-1deg)}
  .swoosh{position:absolute;left:0;top:282px;width:600px;height:70px}
  .panel{position:absolute;background:var(--navy);color:#fff;border-radius:14px}
  .panel ul{list-style:none}
  .panel li{position:relative;padding-left:12px;font-weight:600}
  .panel li::before{content:"";position:absolute;left:0;top:6px;width:5px;height:5px;background:#fff}
  .panel b{font-weight:800}
  .no-list{left:362px;top:194px;width:210px;padding:12px 10px 12px 14px}
  .no-list li{font-size:11.5px;line-height:1.32}
  .terms{left:370px;top:508px;width:218px;padding:16px 12px 16px 18px}
  .terms li{font-size:12.5px;line-height:1.38}
  .program-tag{position:absolute;left:46px;top:344px;width:282px;height:46px;background:var(--red);border:3px solid #fff;outline:1px solid var(--red);color:#fff;font-weight:800;font-size:27px;display:flex;align-items:center;justify-content:center;letter-spacing:.5px}
  .headline{position:absolute;left:56px;top:396px;font-family:"Roboto Slab",serif;font-weight:800;color:var(--navy);font-size:30px;letter-spacing:.5px}
  .subhead{position:absolute;left:56px;top:442px;font-family:"Roboto Slab",serif;font-weight:700;color:var(--navy);font-size:20px;line-height:1.15}
  .eligibility{position:absolute;left:56px;top:506px;color:var(--navy);font-size:15px;font-weight:600;line-height:1.25}
  .eligibility b{font-weight:800}
  .rate{position:absolute;left:382px;top:412px;width:210px;height:90px;color:var(--navy)}
  .rate svg{position:absolute;left:0;top:2px}
  .rate-head{position:absolute;left:68px;top:0;font-weight:800;font-size:16px;line-height:1.05}
  .rate-head span{font-size:20px}
  .rate-note{position:absolute;left:4px;top:58px;width:210px;font-size:11.5px;font-weight:700;line-height:1.3}
  .brand{position:absolute;left:50px;top:584px;display:flex;align-items:center;gap:6px}
  .brand-mark{width:18px;height:18px;background:var(--navy)}
  .brand-name{font-family:"Roboto Slab",serif;font-weight:700;color:var(--navy);font-size:14px;white-space:nowrap}
  .contact{position:absolute;left:228px;top:570px;width:136px;color:var(--navy);font-size:11px;line-height:1.35;font-style:normal;white-space:nowrap}
  .contact .officer{font-weight:600}
  .contact .phone{font-weight:700}
  .fine-print{position:absolute;left:50px;top:640px;width:306px;font-size:7px;line-height:1.35;color:var(--fine)}
</style>
</head>
<body>
<main class="flyer">
  <div class="hero-photo" role="img" aria-label="Stock photo of a cheering group of business people holding a blank poster board"></div>
  <div class="poster-board"></div>
  <div class="stamp">100%<br>FUNDED</div>

  <svg class="swoosh" viewBox="0 0 600 70" preserveAspectRatio="none" aria-hidden="true">
    <path d="M0 48 Q300 0 600 10 L600 70 L0 70 Z" fill="#ffffff"/>
    <path d="M0 44 Q300 -4 600 6 L600 14 Q300 6 0 52 Z" fill="var(--navy)"/>
    <path d="M0 56 Q300 12 600 20 L600 23 Q300 16 0 60 Z" fill="#c9d3e6"/>
  </svg>

  <section class="panel no-list">
    <ul>
      <li><b>NO</b> Tax Returns</li>
      <li><b>NO</b> 4506-T</li>
      <li><b>NO</b> Cash-Out Restrictions</li>
      <li><b>NO</b> Cash Reserves Required</li>
      <li><b>NO</b> Limit on Number of Properties owned or financed</li>
      <li><b>NO</b> DTI Calculation</li>
      <li><b>NO</b> Seasoned Funds</li>
      <li><b>NO</b> Asset Disclosures (Purchase)</li>
    </ul>
  </section>

  <div class="program-tag">STATED INCOME</div>
  <h1 class="headline">FAST &amp; EASY</h1>
  <h2 class="subhead">PURCHASE &amp;<br>CASH OUT REFINANCE</h2>
  <p class="eligibility"><b>Non-owner</b> SFR/Condo/2-4 Units<br>5+ Units &amp; Commercial – Ask for Details</p>

  <div class="rate">
    <svg width="58" height="52" viewBox="0 0 58 52" aria-hidden="true">
      <path d="M4 26 L29 4 L54 26" fill="none" stroke="var(--navy)" stroke-width="5" stroke-linejoin="round"/>
      <rect x="12" y="24" width="34" height="26" fill="none" stroke="var(--navy)" stroke-width="4"/>
      <path d="M19 36 L27 43 L41 28" fill="none" stroke="var(--navy)" stroke-width="5" stroke-linecap="round"/>
    </svg>
    <div class="rate-head">RATES<br>AS LOW AS<br><span>6.49%</span></div>
    <p class="rate-note">3 &amp; 5 Year Fixed ARM –<br>30 Year Amortization</p>
  </div>

  <section class="panel terms">
    <ul>
      <li>Max Rebate 2%</li>
      <li>Max 70% Loan-to-value</li>
      <li>650 Min Credit Score</li>
      <li>Loan Amounts $100,000 to $2,000,000</li>
      <li>Lending to Corporations, LLC, Partnership &amp; Individuals</li>
    </ul>
  </section>

  <div class="brand">
    <span class="brand-mark"></span>
    <span class="brand-name">BrightOak Lending</span>
  </div>
  <address class="contact">
    <div class="officer">Marcus Delaney</div>
    <div class="phone">888-555-0142</div>
    <div>marcus@brightoak.com</div>
    <div>BRE #02468135</div>
  </address>

  <p class="fine-print">Intended for mortgage professional use only and not intended for consumer use as defined by applicable regulation. Financing subject to credit evaluation, approval of collateral and other requirements. Terms subject to change without notice. BrightOak Lending NMLS 000000, 4500 Meadow Park Drive, Suite 210, Irvine, CA 92600.</p>
</main>
</body>
</html>
```